Hi,

I have just started up a business called VOLMIRA in Melbourne. We run fun street art tours around Melbourne's CBD.

I need to create a design for the back side of my business cards. I have designed the front side (simply with my logo) however, I am having trouble designing the reverse side in a professional manner. I have attached pictures of what I have done.

The picture attached titled "VOLMIRA Business Cards Back" has all the information that I require on the back side of my business cards; although displayed in an amateur and simple way. As displayed in the picture, I need: the VOLMIRA logo, the website URL, the booking details (phone - 0468 152 837 & email - bookings@volmira-example.com.au) and the service description ($20, One Hour, Tours Daily, Meet at Halberton St Station). I would also like to use the font in the picture supplied which is "source-sans-pro".

The VOLMIRA tours are for tourists and are relaxed, entertaining and fun! I would like the design to reflect this.

Target Market(s)

Backpackers & University Students

Industry/Entity Type

Business

Requirements
Must have
• The VOLMIRA logo, the website URL, the booking details (phone - 0468 152 837 & email - bookings@volmira-example.com.au) and the service description ($20, One Hour, Tours Daily, Meet at Halberton St Station).

```html
<!DOCTYPE html>
<html lang="en">
<head>
<meta charset="utf-8">
<title>VOLMIRA – Business Card Back</title>
<link rel="stylesheet" href="https://fonts.googleapis.com/css2?family=Source+Sans+3:wght@600;700&display=swap">
<style>
  :root {
    --backdrop: #2f2724;
    --card-light: #ececec;
    --card-mid: #e0e0e0;
    --ink: #222222;
    --accent: #e8533f;
    --pattern-warm: rgba(232, 160, 140, 0.22);
    --pattern-grey: rgba(180, 180, 180, 0.16);
  }
  html, body {
    margin: 0;
    width: 1200px;
    height: 1000px;
    overflow: hidden;
    background: var(--backdrop);
    font-family: "Source Sans 3", "Source Sans Pro", sans-serif;
  }
  .card {
    position: absolute;
    left: 260px;
    top: 304px;
    width: 682px;
    height: 393px;
    overflow: hidden;
    background: linear-gradient(90deg, var(--card-mid) 0%, var(--card-light) 50%, var(--card-mid) 100%);
    color: var(--ink);
    font-weight: 600;
  }
  .pattern-area {
    position: absolute;
    top: 0;
    width: 300px;
    height: 393px;
    background:
      radial-gradient(ellipse at 50% 30%, var(--pattern-warm) 0%, transparent 55%),
      radial-gradient(ellipse at 50% 75%, var(--pattern-grey) 0%, transparent 60%);
  }
  .pattern-area--left { left: 0; }
  .pattern-area--right { right: 0; }

  .booking-call {
    position: absolute;
    left: 40px;
    top: 35px;
    width: 154px;
    font-size: 15px;
    line-height: 20px;
    text-align: center;
  }
  .booking-email {
    position: absolute;
    right: 42px;
    top: 32px;
    font-size: 15px;
    line-height: 20px;
  }
  .brand-name {
    position: absolute;
    left: 0;
    right: 0;
    top: 152px;
    text-align: center;
    font-size: 58px;
    font-weight: 700;
    letter-spacing: 3px;
    line-height: 1;
    color: var(--ink);
  }
  .service-item {
    position: absolute;
    top: 245px;
    font-size: 18px;
    line-height: 22px;
  }
  .service-item .label { display: block; color: var(--accent); }
  .price { left: 173px; top: 256px; }
  .price .currency { color: var(--accent); }
  .service-tours { left: 229px; }
  .service-length { left: 307px; }
  .service-meet { left: 378px; }
  .website {
    position: absolute;
    left: 0;
    right: 0;
    top: 340px;
    text-align: center;
    font-size: 15px;
    line-height: 20px;
  }
</style>
</head>
<body>
  <main class="card">
    <div class="pattern-area pattern-area--left" role="img" aria-label="Faint decorative pattern area in soft peach and grey"></div>
    <div class="pattern-area pattern-area--right" role="img" aria-label="Faint decorative pattern area in soft peach and grey"></div>

    <div class="booking-call">Call Remy to BOOK NOW<br>0468 152 837</div>
    <div class="booking-email">bookings@volmira-example.com.au</div>

    <div class="brand-name">VOLMIRA</div>

    <div class="service-item price"><span class="currency">$</span>20</div>
    <div class="service-item service-tours"><span class="label">Tours</span>Daily</div>
    <div class="service-item service-length"><span class="label">One</span>Hour</div>
    <div class="service-item service-meet"><span class="label">Meet at</span>Halberton Station</div>

    <div class="website">www.volmira-example.com.au</div>
  </main>
</body>
</html>
```